Velvet Paws Website - Boutique online pet store for both owners, their homes and their dogs

I need a high end online store for the sale of dog products (collars, leashes, coats etc), products for their owners (pyjamas, cosmetic bags, pencil cases, gift wrapping paper, greeting cards etc) and the owners home (ring holders, cushion covers, throws etc).

Please peruse the following website for a vauge idea of slightly similar stores:

Mybeaglecorner.com.au
Pebblepuphaven.com.au
Terrierplace.com.au
Tallhound.co.za

Please keep in mind these are breed specific sites. I intend for the business to sell to trending dog breeds, for example, currently in Australia, French Bulldogs and Dachshunds are trending; therefore this will be the business's current focus.

I also intend for this website to be more elegant and refined than the websites mentioned above. Similar to top names brands, with a hint of cuteness to appeal to the animal lover within customers.

Target Market(s)

Velvet Paws' target market is majority females, late 20's - 40's, either single, in a relationship, or with children who have left the home. They own small and pampered dogs and treat these dogs like their children. They will have a high disposable income.

I want the brand to attract elitist clientele. Comment has been made that people mightn't be able to spell Velvet when searching for the website; those are not the type of customers I want to attract. I think it may be difficult to encapsulate these two target ideas into the brand; I'd like is to appeal to both the 'Melbourne Socialite' and the Noosa stereotype of "I'm too cool to show it, but I really care what you think"

The products will be, for the most part, unique to the market, a few examples include:

custom hand made collars and leads reflecting current human fashion trends;
leather coats for dogs;
flannel pyjamas for dog;
chef's hats for dogs;
furniture which incorporates dogs beds (blanket box, coffee table, bedside table)
bags, cushions, throw rugs, pyjamas made from various dog print fabrics;
fine leather handbags and purses with various and discreet dog themed embellishments;
custom gift wrapping paper etc etc

Amazing customer service and high quality are two of the core values of Velvet Paws.

The business will be run through the website as well as high-end markets around Brisbane, Gold Coast and Sunshine Coast.

Colors
eea4c8
ffffff
e34197

Requirements
Must have
• MUST BE FULLY OPERATIONAL ON COMPLETION. I own the domain name www.velvetpaws-example.com.au. Needs to be functioning on this domain with an operational online store using Payvora.
• Must also be mobile friendly.
• Pages:
• For your pup (shopping page)
• For your home (shopping page)
• For you (shopping page)
• Stationery
• Contact us
• I am open to better and more creative page names.
• MUST have an easy to operate back end that I can use to update products as and when required.

```html
<!DOCTYPE html>
<html lang="en">
<head>
<meta charset="utf-8">
<title>Velvet Paws</title>
<link href="https://fonts.googleapis.com/css2?family=Open+Sans:wght@400;600;700&family=PT+Sans:wght@400;700&display=swap" rel="stylesheet">
<style>
:root{
  --pink:#e34197;
  --pink-dark:#b8276f;
  --pink-soft:#eea4c8;
  --white:#ffffff;
  --page:#efeef0;
  --ink:#222222;
  --text:#555555;
  --black:#0d0d0d;
  --line:#dddddd;
}
*{box-sizing:border-box;margin:0;padding:0}
html,body{width:1200px;height:2612px;overflow:hidden}
body{background:var(--page);font-family:"PT Sans",sans-serif;color:var(--text);position:relative}
.wrap{position:absolute;left:111px;width:978px}
a{color:inherit;text-decoration:none}

/* header */
.site-header{position:absolute;top:0;left:0;width:1200px;height:99px}
.brand{position:absolute;left:111px;top:36px;display:flex;align-items:center;gap:10px}
.brand-dot{width:40px;height:40px;border-radius:50%;background:var(--pink)}
.brand-name{font-family:"Open Sans",sans-serif;font-weight:600;font-size:26px;color:var(--ink)}
.account-links{position:absolute;left:858px;top:47px;font-family:"Open Sans",sans-serif;font-size:11px;color:var(--ink);letter-spacing:.3px}
.account-links span{margin:0 5px}
.cart-bowl{position:absolute;left:1031px;top:38px;width:56px;height:32px}

/* nav */
.main-nav{position:absolute;top:99px;left:0;width:1200px;height:58px;background:var(--black)}
.main-nav ul{list-style:none;position:absolute;left:111px;top:0;height:58px;display:flex;align-items:center}
.main-nav li{font-family:"Open Sans",sans-serif;font-size:12px;font-weight:600;color:var(--white);margin-right:48px;text-transform:uppercase}
.main-nav li.active{color:var(--pink);background:#2a2a2a;border-radius:20px;padding:12px 6px;margin-right:40px}
.search{position:absolute;left:911px;top:8px;width:175px;height:42px;background:var(--white);border:1px solid var(--line);font-size:11px;color:#999;padding:13px 16px}
.search svg{position:absolute;right:14px;top:14px}

/* hero */
.hero{position:absolute;top:157px;left:0;width:1200px;height:473px;background:linear-gradient(90deg,#eadde3 0%,#ecdfe5 40%,#efe6ea 46%,rgba(0,0,0,0) 46%)}
.hero-photo{position:absolute;left:520px;top:0;width:680px;height:473px;background:linear-gradient(180deg,#c9b9a6 0%,#a99880 30%,#7f9a4c 62%,#5f8a36 100%)}
.hero-fade{position:absolute;left:500px;top:0;width:140px;height:473px;background:linear-gradient(90deg,#ecdfe5,rgba(236,223,229,0))}
.hero-title{position:absolute;left:111px;top:168px;display:flex;align-items:center;gap:10px;font-family:"Open Sans",sans-serif;font-size:35px;font-weight:400;color:#333}
.hero-text{position:absolute;left:111px;top:232px;width:460px;font-size:13px;line-height:30px;color:#555}
.hero-link{position:absolute;left:111px;top:301px;font-family:"Open Sans",sans-serif;font-size:14px;font-weight:600;color:#333;display:flex;gap:6px;align-items:center}
.slider-dots{position:absolute;left:545px;top:432px;display:flex;gap:13px}
.slider-dots i{width:16px;height:14px;border-radius:50% 50% 40% 40%;background:#777}
.slider-dots i.on{background:var(--pink)}

/* categories */
.categories{top:678px;display:flex;justify-content:space-between}
.category{position:relative;width:309px;height:193px;border:3px solid var(--white);box-shadow:0 1px 3px rgba(0,0,0,.15);overflow:hidden}
.category .photo{position:absolute;inset:0}
.category h3{position:absolute;left:20px;bottom:40px;font-family:"Open Sans",sans-serif;font-size:33px;font-weight:600;color:var(--white);letter-spacing:-.5px;line-height:1}
.category p{position:absolute;left:20px;bottom:16px;font-size:16px;color:var(--white)}

/* tabs */
.tabs{top:925px;display:flex;justify-content:center;gap:36px;font-family:"Open Sans",sans-serif;font-size:20px;color:#222}
.tabs span{padding-bottom:8px}
.tabs .current{color:var(--pink);border-bottom:2px solid var(--pink)}

/* products */
.products{top:1003px;display:grid;grid-template-columns:repeat(4,227px);column-gap:23.6px;row-gap:35px}
.product{height:316px;background:var(--white);border:1px solid var(--line);box-shadow:0 1px 3px rgba(0,0,0,.06);padding:17px;text-align:center}
.product .thumb{height:118px;border:1px solid var(--line);box-shadow:inset 0 0 0 4px #f6f6f6;position:relative;background:var(--white)}
.product .thumb div{position:absolute;left:30%;right:30%;top:30%;bottom:30%;border-radius:10px}
.product p{margin-top:20px;font-size:11.5px;line-height:26px;color:#444;height:52px}
.product .price{margin-top:6px;font-family:"Open Sans",sans-serif;font-size:15px;font-weight:600;color:var(--pink)}
.btn-cart{margin:11px auto 0;width:190px;height:44px;background:linear-gradient(180deg,#d8448f,var(--pink-dark));color:var(--white);font-family:"Open Sans",sans-serif;font-size:12px;display:flex;align-items:center;justify-content:center;gap:6px}

/* about */
.about{position:absolute;top:1723px;left:0;width:1200px;height:327px;background:var(--pink)}
.about h2{position:absolute;left:111px;top:48px;display:flex;align-items:center;gap:10px;font-family:"Open Sans",sans-serif;font-size:24px;font-weight:400;color:var(--white)}
.about p{position:absolute;left:111px;top:97px;width:540px;font-size:11.5px;line-height:22px;color:var(--white)}
.about .more{position:absolute;left:111px;top:255px;font-family:"Open Sans",sans-serif;font-size:15px;font-weight:600;color:var(--white);display:flex;gap:6px;align-items:center}
.about-photo{position:absolute;left:685px;top:19px;width:515px;height:293px;background:linear-gradient(135deg,#e9eef6 0%,#6c8fd6 35%,#3a3c8c 60%,#9aaee4 100%)}

/* newsletter */
.newsletter{top:2103px}
.newsletter h2{display:flex;align-items:center;gap:12px;font-family:"Open Sans",sans-serif;font-size:24px;font-weight:400;color:#222}
.newsletter p{margin-top:17px;font-size:11.5px;line-height:26px;color:#444}
.signup{margin-top:22px;display:flex;gap:19px}
.field{width:309px;height:48px;background:var(--white);border:1px solid var(--line);font-size:11px;color:#999;padding:16px 18px}
.btn-subscribe{width:200px;height:48px;background:linear-gradient(180deg,#d8448f,var(--pink-dark));color:var(--white);font-family:"Open Sans",sans-serif;font-size:15px;font-weight:600;display:flex;align-items:center;justify-content:center}

/* footer */
.site-footer{position:absolute;top:2312px;left:0;width:1200px;height:224px;background:var(--white)}
.footer-col{position:absolute;top:36px}
.footer-col h4{font-family:"Open Sans",sans-serif;font-size:15px;font-weight:600;color:#222}
.footer-col ul{list-style:none;margin-top:9px}
.footer-col li{font-size:10.5px;color:#444;height:34.5px;display:flex;align-items:center;gap:6px}
.footer-col li::before{content:"";width:5px;height:5px;border-top:2px solid var(--pink);border-right:2px solid var(--pink);transform:rotate(45deg)}
.social{display:flex;gap:21px;margin-top:18px}
.social span{width:36px;height:36px;border-radius:3px;box-shadow:0 1px 2px rgba(0,0,0,.3)}
.sq-a{background:#2f4a8a}.sq-b{background:#37a5d8}.sq-c{background:#1f6fa6}
.sq-d{background:#eebb3a;display:flex;align-items:center;justify-content:center}

/* bottom bar */
.bottom-bar{position:absolute;top:2536px;left:0;width:1200px;height:76px;background:var(--pink)}
.copyright{position:absolute;left:111px;top:31px;font-size:10.5px;color:var(--white)}
.payments{position:absolute;left:888px;top:22px;display:flex;gap:11px}
.payments span{width:43px;height:30px;background:var(--white);border-radius:3px;font-family:"Open Sans",sans-serif;font-size:8px;font-weight:600;color:#333;display:flex;align-items:center;justify-content:center}
</style>
</head>
<body>

<header class="site-header">
  <div class="brand"><span class="brand-dot"></span><span class="brand-name">Velvet Paws</span></div>
  <div class="account-links">LOGIN<span>|</span>REGISTER<span>|</span>WISHLIST</div>
  <svg class="cart-bowl" viewBox="0 0 56 32" aria-label="Cart (0)">
    <path d="M4 8 H52 L47 28 H9 Z" fill="#e34197"/>
    <ellipse cx="28" cy="8" rx="24" ry="5" fill="#f06aae"/>
    <text x="28" y="22" text-anchor="middle" font-family="Open Sans,sans-serif" font-size="8" fill="#fff">(0)</text>
  </svg>
</header>

<nav class="main-nav">
  <ul>
    <li class="active">Home</li>
    <li>For your pup</li>
    <li>For your home</li>
    <li>For you</li>
    <li>Stationery</li>
    <li>Contact us</li>
  </ul>
  <div class="search">Search...
    <svg width="12" height="12" viewBox="0 0 12 12"><circle cx="5" cy="5" r="3.8" fill="none" stroke="#999" stroke-width="1.5"/><path d="M8 8 L11 11" stroke="#999" stroke-width="1.5"/></svg>
  </div>
</nav>

<section class="hero">
  <div class="hero-photo" role="img" aria-label="Happy tan dog lying on green grass wearing a collar"></div>
  <div class="hero-fade"></div>
  <h1 class="hero-title">
    <svg width="58" height="30" viewBox="0 0 58 30"><rect x="3" y="7" width="52" height="17" rx="8" fill="none" stroke="#444" stroke-width="5"/><rect x="22" y="3" width="14" height="24" rx="2" fill="#444"/></svg>
    DOG COLLARS
  </h1>
  <p class="hero-text">Lorem ipsum dolor sit amet, consectetur adipiscing elit. Sed molestie aliquet pretium. Nam in metus dignissim, placerat purus eu, mollis turpis.</p>
  <a class="hero-link"><svg width="12" height="12" viewBox="0 0 12 12" fill="#e34197"><circle cx="3" cy="3" r="1.5"/><circle cx="6" cy="1.8" r="1.5"/><circle cx="9" cy="3" r="1.5"/><ellipse cx="6" cy="8" rx="3.3" ry="2.8"/></svg>OUR PRODUCTS</a>
  <div class="slider-dots"><i></i><i></i><i class="on"></i><i></i></div>
</section>

<section class="wrap categories">
  <article class="category">
    <div class="photo" role="img" aria-label="Small white dog on a purple mat" style="background:linear-gradient(180deg,#8a7c73,#6a5a66 60%,#5c4e63)"></div>
    <h3>DOG BEDS</h3><p>Get % 30 Offer</p>
  </article>
  <article class="category">
    <div class="photo" role="img" aria-label="Person walking a dog on a leash along a track" style="background:linear-gradient(180deg,#9fa9b5,#7a6f6a 50%,#7a4a44)"></div>
    <h3>DOG LEASHES</h3><p>Get % 24 Offer</p>
  </article>
  <article class="category">
    <div class="photo" role="img" aria-label="Dog wearing a collar on a lawn" style="background:linear-gradient(180deg,#b8b8b2,#8a8e6c 55%,#5f7a3a)"></div>
    <h3>DOG COLLARS</h3><p>Get % 30 Offer</p>
  </article>
</section>

<div class="wrap tabs"><span class="current">FATURED PRODUCTS</span><span>ONSALE</span><span>BESTSELLER</span></div>

<section class="wrap products">
  <article class="product"><div class="thumb" role="img" aria-label="Brown leather collar with bone charm"><div style="background:#7a4a2a"></div></div><p>Lorem ipsum dolor sit amet,<br>consectetur adipiscing</p><div class="price">$ 8.00</div><a class="btn-cart"><svg width="12" height="11" viewBox="0 0 12 11" fill="#fff"><path d="M0 0H2.5L3.2 2H12L10.5 7H4L2 1H0Z"/><circle cx="4.5" cy="9.5" r="1.2"/><circle cx="9.5" cy="9.5" r="1.2"/></svg>ADD TO CART</a></article>
  <article class="product"><div class="thumb" role="img" aria-label="Black leash with silver clip"><div style="background:#2a2a2a"></div></div><p>Fusce non lectus eu turpis consequat<br>egestas a nec quam</p><div class="price">$ 12.00</div><a class="btn-cart"><svg width="12" height="11" viewBox="0 0 12 11" fill="#fff"><path d="M0 0H2.5L3.2 2H12L10.5 7H4L2 1H0Z"/><circle cx="4.5" cy="9.5" r="1.2"/><circle cx="9.5" cy="9.5" r="1.2"/></svg>ADD TO CART</a></article>
  <article class="product"><div class="thumb" role="img" aria-label="Black slip leash"><div style="background:#333"></div></div><p>Aliquam et odio ligula phasellus<br>varius massa nunc</p><div class="price">$ 11.00</div><a class="btn-cart"><svg width="12" height="11" viewBox="0 0 12 11" fill="#fff"><path d="M0 0H2.5L3.2 2H12L10.5 7H4L2 1H0Z"/><circle cx="4.5" cy="9.5" r="1.2"/><circle cx="9.5" cy="9.5" r="1.2"/></svg>ADD TO CART</a></article>
  <article class="product"><div class="thumb" role="img" aria-label="Dark leather collar with name plate"><div style="background:#4a3328"></div></div><p>Curabitur ut purus commodo,<br>pretium nibh a, rhoncus ex</p><div class="price">$ 8.00</div><a class="btn-cart"><svg width="12" height="11" viewBox="0 0 12 11" fill="#fff"><path d="M0 0H2.5L3.2 2H12L10.5 7H4L2 1H0Z"/><circle cx="4.5" cy="9.5" r="1.2"/><circle cx="9.5" cy="9.5" r="1.2"/></svg>ADD TO CART</a></article>
  <article class="product"><div class="thumb" role="img" aria-label="Red leash"><div style="background:#d0303a"></div></div><p>Vivamus porttitor turpis placerat<br>ipsum tempor</p><div class="price">$ 12.00</div><a class="btn-cart"><svg width="12" height="11" viewBox="0 0 12 11" fill="#fff"><path d="M0 0H2.5L3.2 2H12L10.5 7H4L2 1H0Z"/><circle cx="4.5" cy="9.5" r="1.2"/><circle cx="9.5" cy="9.5" r="1.2"/></svg>ADD TO CART</a></article>
  <article class="product"><div class="thumb" role="img" aria-label="Brass tag on a key ring"><div style="background:#b08a3a"></div></div><p>Curabitur odio turpis maximus ut<br>enim eu, sodales</p><div class="price">$ 8.00</div><a class="btn-cart"><svg width="12" height="11" viewBox="0 0 12 11" fill="#fff"><path d="M0 0H2.5L3.2 2H12L10.5 7H4L2 1H0Z"/><circle cx="4.5" cy="9.5" r="1.2"/><circle cx="9.5" cy="9.5" r="1.2"/></svg>ADD TO CART</a></article>
  <article class="product"><div class="thumb" role="img" aria-label="Brown collar with blue tag"><div style="background:#5a3226"></div></div><p>Aenean nec enim ut ipsum<br>pellentesque porta</p><div class="price">$ 14.00</div><a class="btn-cart"><svg width="12" height="11" viewBox="0 0 12 11" fill="#fff"><path d="M0 0H2.5L3.2 2H12L10.5 7H4L2 1H0Z"/><circle cx="4.5" cy="9.5" r="1.2"/><circle cx="9.5" cy="9.5" r="1.2"/></svg>ADD TO CART</a></article>
  <article class="product"><div class="thumb" role="img" aria-label="Black collar with gold plate"><div style="background:#2a2418"></div></div><p>Lorem ipsum dolor sit amet,<br>consectetur adipiscing</p><div class="price">$ 8.00</div><a class="btn-cart"><svg width="12" height="11" viewBox="0 0 12 11" fill="#fff"><path d="M0 0H2.5L3.2 2H12L10.5 7H4L2 1H0Z"/><circle cx="4.5" cy="9.5" r="1.2"/><circle cx="9.5" cy="9.5" r="1.2"/></svg>ADD TO CART</a></article>
</section>

<section class="about">
  <h2><svg width="24" height="24" viewBox="0 0 24 24"><circle cx="12" cy="12" r="11" fill="#fff"/></svg>ABOUT</h2>
  <p>Lorem ipsum dolor sit amet, consectetur adipiscing elit. Morbi vel leo ut tellus auctor semper. Cras eget tortor tristique, placerat erat sit amet, vulputate justo. Sed non sapien eu massa volutpat scelerisque. Nulla egestas elit efficitur, dapibus sem vitae, vulputate tellus. Aenean ut mauris sem. Etiam et congue tortor. Proin nisi enim, placerat in varius eu, ullamcorper euismod ligula. Fusce ullamcorper, metus sit amet condimentum tempus, magna ante semper elit, ut scelerisque mauris diam.</p>
  <a class="more"><svg width="12" height="12" viewBox="0 0 12 12" fill="#fff"><circle cx="3" cy="3" r="1.5"/><circle cx="6" cy="1.8" r="1.5"/><circle cx="9" cy="3" r="1.5"/><ellipse cx="6" cy="8" rx="3.3" ry="2.8"/></svg>READ MORE</a>
  <div class="about-photo" role="img" aria-label="Dog wearing sunglasses against a blue splash backdrop"></div>
</section>

<section class="wrap newsletter">
  <h2><svg width="22" height="16" viewBox="0 0 22 16"><rect width="22" height="16" rx="2" fill="#e34197"/><path d="M1 2 L11 9 L21 2" fill="none" stroke="#fff" stroke-width="1.8"/></svg>SIGNUP OUR NEWSLETTER</h2>
  <p>Lorem ipsum dolor sit amet, consectetur adipiscing elit. Morbi vel leo ut tellus auctor semper. Cras eget tortor tristique, placerat erat sit amet, vulputate justo. Sed non sapien eu massa volutpat scelerisque. Nulla egestas elit efficitur, dapibus sem vitae, vulputate tellus. Aenean ut mauris sem. Etiam et congue tortor.</p>
  <div class="signup"><div class="field">Name</div><div class="field">Email Address</div><a class="btn-subscribe">SUBSCRIBE</a></div>
</section>

<footer class="site-footer">
  <div class="footer-col" style="left:111px"><h4>PRODUCTS</h4><ul><li>Lorem ipsum dolor sit amet</li><li>consectetur adipiscing elit</li><li>Morbi et elit ut diam bibendum</li><li>Dictum eget ut nisi</li></ul></div>
  <div class="footer-col" style="left:347px"><h4>QUICK LINKS</h4><ul><li>Morbi et elit ut diam bibendum</li><li>Dictum eget ut nisi</li><li>Lorem ipsum dolor sit amet</li><li>consectetur adipiscing elit</li></ul></div>
  <div class="footer-col" style="left:584px"><h4>OUR SHOP</h4><ul><li>Dictum eget ut nisi</li><li>Lorem ipsum dolor sit amet</li><li>consectetur adipiscing elit</li><li>Morbi et elit ut diam bibendum</li></ul></div>
  <div class="footer-col" style="left:840px"><h4>FOLLOW ON</h4>
    <div class="social"><span class="sq-a"></span><span class="sq-b"></span><span class="sq-c"></span><span class="sq-d"><svg width="18" height="13" viewBox="0 0 18 13"><rect width="18" height="13" rx="1" fill="#fff"/><path d="M1 1 L9 7 L17 1" fill="none" stroke="#eebb3a" stroke-width="1.5"/></svg></span></div>
  </div>
</footer>

<div class="bottom-bar">
  <div class="copyright">Copyright©2016 Velvet Paws. All rights reserved</div>
  <div class="payments"><span>Payvora</span><span>Mestra</span><span>Cardmont</span><span>Vistro</span></div>
</div>

</body>
</html>
```